Fundraiser Brochure for Candle Company

We are a mid-sized candle company. We have been doing fundraisers for many years and need a new design/look for our brochure. Please don't design it to mimic our website - I want that updated as well. I'm looking for more of a Marisa Thornbury, Juniper Hollow look. I want this to be 5.5 w X 8.5 h size but that isn't an option here. I called Quick Press Prints and they said to just put it in the notes - OK there ya go!! We do not need an order form with this as we are going to make a separate sheet to insert for the order form. I'd like the products types (barn candles, barn brick sets, reflective light candles, soup) each to have their own page. Rooms Sprays and Diffusers can go on the same page since there are only a few of each to select from. The fragrance descriptions can be all on 1 page since there are repeats in the different product types. The soup is a big seller for us :) Please feel free to do what you'd like to with the pix. I know the quality isn't amazing but it's all I have right now. Thank you!!! Dorinda

Font styles to use
Serif

Requirements
Nice to have
• I listed what I'd like in the project descriptions

```html
<!DOCTYPE html>
<html lang="en">
<head>
<meta charset="utf-8">
<title>Fragrance Descriptions</title>
<link href="https://fonts.googleapis.com/css2?family=Noto+Serif:wght@400;700&display=swap" rel="stylesheet">
<style>
  :root {
    --paper: #ffffff;
    --wash-warm: #fbeee8;
    --wash-mid: #fdfbf2;
    --wash-cool: #eef6fb;
    --panel: #f7f8df;
    --panel-edge: #b5dd8a;
    --section: #8cc63f;
    --code: #c9dc3b;
    --rule: #9fd06a;
    --heading: #3aae4a;
    --ink: #2b2b2b;
    --white: #ffffff;
  }
  * { box-sizing: border-box; margin: 0; padding: 0; }
  html, body { width: 934px; height: 1200px; overflow: hidden; background: var(--paper); }
  body { position: relative; font-family: "Noto Serif", Georgia, serif; color: var(--ink); }

  .ribbon-backdrop {
    position: absolute; inset: 0;
    background: linear-gradient(160deg, var(--wash-warm) 0%, var(--wash-mid) 50%, var(--wash-cool) 100%);
  }

  .fragrance-table {
    position: absolute; left: 130px; top: 116px; width: 726px; height: 994px;
    background: var(--panel);
    box-shadow: inset 0 0 10px 4px var(--panel-edge);
    padding: 0 6px;
  }
  .table-head {
    display: grid; grid-template-columns: 178px 70px 1fr;
    height: 26px; align-items: center;
    font-weight: 700; font-size: 14.5px; color: var(--heading); text-align: center;
  }
  .section-bar {
    height: 24px; background: var(--section); color: var(--white);
    font-weight: 700; font-size: 16px; text-align: center; line-height: 24px;
  }
  .row {
    display: grid; grid-template-columns: 178px 70px 1fr;
    border-bottom: 1px solid var(--rule);
  }
  .row.last { border-bottom: none; }
  .name { font-size: 16.5px; padding: 4px 0 0 1px; align-self: start; white-space: nowrap; }
  .row.centered .name { align-self: center; padding-top: 0; }
  .code {
    background: var(--code); font-size: 16.5px;
    display: flex; align-items: center; justify-content: center;
  }
  .desc { font-size: 14.2px; line-height: 19.6px; padding: 2px 0 2px 6px; white-space: nowrap; }
</style>
</head>
<body>
<div class="ribbon-backdrop" role="img" aria-label="Decorative background of soft pastel curved ribbons in peach, tan, green, orange, blue and yellow"></div>

<main class="fragrance-table">
  <div class="table-head"><span>CATEGORY</span><span>CODE</span><span>DESCRIPTION</span></div>

  <div class="section-bar">FRUITY</div>
  <div class="row centered" style="height:44px"><div class="name">Strawberry Rhubarb</div><div class="code">STR</div><div class="desc">A country patch of hand picked strawberries blended with<br>freshly cut stalks of rhubarb, create an irresistable fragrance.</div></div>
  <div class="row centered" style="height:63px"><div class="name">Lemon Chiffon</div><div class="code">LEM</div><div class="desc">It's no secret that a farm fresh baked delicacy is simply ex-<br>quisite. Tarty sweet fragrance collides with the perfect velvet<br>smooth texture, molding this into an alluring candle.</div></div>
  <div class="row centered" style="height:25px"><div class="name">Pearberry</div><div class="code">PEA</div><div class="desc">A fresh, fruity, fragrant blend of red berries and ripe pears.</div></div>
  <div class="row centered last" style="height:62px"><div class="name">Ruby Red</div><div class="code">RUB</div><div class="desc">A scoop of the tangy, juicy grapefruit pulp that drips from<br>your hand and awakens your tastebuds, poured in the soft<br>orange and pink hue of the beautiful rind.</div></div>

  <div class="section-bar">BAKED</div>
  <div class="row" style="height:63px"><div class="name">Grandma's Kitchen</div><div class="code">GRA</div><div class="desc">Revisit moments gone by in your grandma's kitchen. The<br>aroma of sweet baked sugar cookies with a hint of savory<br>cinnamon.</div></div>
  <div class="row" style="height:62px"><div class="name">Maple Pecan</div><div class="code">MAP</div><div class="desc">Just wait until you are greeted by the unmistakably delicious<br>aroma of rich and creamy maple, laden with ripe pecans,<br>brought together in one exquisitely delectable scent.</div></div>
  <div class="row" style="height:43px"><div class="name">Amish Cookie</div><div class="code">AMI</div><div class="desc">Just-baked sugar cookies fill the air with a delightful blend of<br>almond, cinnamon, vanilla, and dark brown sugar.</div></div>
  <div class="row last" style="height:62px"><div class="name">Cinnamon Stick</div><div class="code">CIN</div><div class="desc">Nothing beats the classic spicy scent of warm cinnamon,<br>clove, and ginger. The pure indulgence of this fragrance is<br>inviting in any room.</div></div>

  <div class="section-bar">HOLIDAY</div>
  <div class="row" style="height:63px"><div class="name">Christmas Splendor</div><div class="code">CHR</div><div class="desc">Return to the simplicity and beauty of holiday traditions.<br>Blend oranges, cranberries and spices together to create this<br>fabulous festival of scent.</div></div>
  <div class="row" style="height:43px"><div class="name">Jack Frost</div><div class="code">JAC</div><div class="desc">A blast of icy freshness will shock your senses with a chilling<br>combination of peppermint and vanilla.</div></div>
  <div class="row" style="height:63px"><div class="name">Sugar Plum</div><div class="code">SUG</div><div class="desc">This holiday favorite is sure to leave sugarplums dancing in<br>your head! A celebration of orange, persimmon, ripe plums,<br>and succulent berries, with a hint of Concord grapes.</div></div>
  <div class="row" style="height:62px"><div class="name">Berry Kisses</div><div class="code">BER</div><div class="desc">Oh the sweet flavor of Chocolate covered Raspberries. You<br>can almost taste them as you burn this beautiful chocolatey<br>brown candle, but there are 0 calories.</div></div>
  <div class="row last" style="height:102px"><div class="name">O Christmas Tree</div><div class="code">OCT</div><div class="desc">OH Christmas Tree you smell soooo wonderful. This will<br>take you back to those days when you had a real tree and it<br>smelled so great that you forgot you would be picking up<br>needles well into the summer!! All of the smell but NO nee-<br>dles to pick up!!</div></div>

  <div class="section-bar">FRESH</div>
  <div class="row" style="height:63px"><div class="name">Citrus &amp; Sea Salt</div><div class="code">CIT</div><div class="desc">Citrus &amp; Sea Salt transports you to the sandy beaches of a<br>soft blue ocean, refreshing you with a sparkling lime drink,<br>rimmed with coarse sea salt.</div></div>
  <div class="row last" style="height:44px"><div class="name">Stress Relief</div><div class="code">REL</div><div class="desc">Take the stress of your day away with this soothing and relax-<br>ing aroma of eucalyptus, fresh mint, sage, and musk.</div></div>
</main>
</body>
</html>
```